Redesign of existing template to align with brand identify

We need page template redesign for our teach English abroad content cluster. Our dev guy created a mockup for a page template, although decent, it needs a designer's touch to elevate it and make sure it aligns with our existing brand identity on the website. The mockup has been created on figma and we would prefer the design files to include figma files.

The designer can either work from scratch or they work on the design we already have on the figma link - https://www.drafmoly-board.net/file/Q7wRpK2mTzVxa9bLcNe4Hd/Teach-English-Abroad-Mockup?node-id=41%3A19&t=pa4uKmWzrTqsYvBn-7

We need a design for both desktop and mobile layout. You can visit our website here https://www.brinvoldlearning.com/ to see our brand colors and style. We want to use a lot of white space on the design with a hint of our brand colors.

Video 1 - https://clipvarno.net/502746318/4d7e1a9c3f >> watch this one first
Video 2 - https://clipvarno.net/502748027/e6a2f05d71

```html
<!DOCTYPE html>
<html lang="en">
<head>
<meta charset="utf-8">
<title>Teach English in South Korea</title>
<link href="https://fonts.googleapis.com/css2?family=Poppins:wght@400;500;600;700;800&display=swap" rel="stylesheet">
<style>
:root{
  --brand:#00d2d6;
  --heading:#6b6b6b;
  --text:#5e5e5e;
  --muted:#777;
  --dark:#1e1e1e;
  --white:#fff;
  --card-shadow:0 2px 12px rgba(0,0,0,.09);
}
*{margin:0;padding:0;box-sizing:border-box}
html,body{width:1200px;height:2618px;overflow:hidden;background:var(--white)}
body{font-family:'Poppins',sans-serif;color:var(--text);position:relative}
.abs{position:absolute}
.hero{left:0;top:0;width:1200px;height:375px;background:radial-gradient(ellipse at 50% 35%,#6f7f34 0%,#3d4b22 35%,#1f2914 70%,#121a0e 100%)}
.hero-title{left:0;top:200px;width:1200px;text-align:center;color:var(--white);font-size:31px;font-weight:700}
.crumbs{left:0;top:261px;width:1200px;text-align:center;color:var(--white);font-size:13px}
.crumbs span.sep{margin:0 9px}
.crumbs .current{color:var(--brand)}
.intro-title{left:0;top:418px;width:1200px;text-align:center;font-size:31px;font-weight:700;color:var(--heading)}
.intro-sub{left:0;top:471px;width:1200px;text-align:center;font-size:15.5px;color:var(--brand)}
.intro-body{left:90px;top:508px;width:1020px;text-align:center;font-size:10px;line-height:13px;color:var(--muted)}
.intro-body p{margin-bottom:13px}
.intro-body a{color:var(--brand);text-decoration:none}
.btn-cyan{background:var(--brand);color:var(--white);font-size:8px;text-transform:uppercase;display:flex;align-items:center;justify-content:center;letter-spacing:.2px}
.intro-btn{left:537px;top:698px;width:126px;height:34px}
.cta{left:0;top:775px;width:1200px;height:332px}
.cta-bg{width:100%;height:100%;background:linear-gradient(90deg,#eceef3 0%,#e6e8ef 45%,#f2f2f2 62%,#dcdde3 80%,#e8d9b8 100%)}
.cta-title{left:81px;top:72px;font-size:25px;font-weight:600;color:var(--dark)}
.cta-text{left:81px;top:120px;width:480px;font-size:13px;line-height:22.5px;color:var(--dark)}
.cta-btn{left:81px;top:203px;width:128px;height:31px;border-radius:16px;background:#d9d9d9;color:var(--dark);font-size:13px;font-weight:600;display:flex;align-items:center;justify-content:center}
.section-title{left:81px;font-size:25.5px;font-weight:700;color:var(--heading)}
.job{width:500px;height:123px;background:var(--white);box-shadow:var(--card-shadow);padding:26px 26px 0}
.job h3{font-size:16px;font-weight:600;line-height:23.5px;color:var(--heading)}
.job .meta{margin-top:9px;font-size:14px;color:var(--muted);display:flex;gap:23px}
.job .meta .loc{color:var(--brand)}
.view-all{left:1040px;top:1804px;width:78px;text-align:right;font-size:15px;color:var(--dark)}
.place{width:248px;height:119px;display:flex;align-items:flex-end;justify-content:center;padding-bottom:8px;color:var(--white);font-size:15.5px;font-weight:600}
.place .ph{position:absolute;inset:0}
.place span{position:relative}
.post{width:248px;height:225px}
.post .ph{height:103px;background:linear-gradient(180deg,#3e4a2c 0%,#2b3322 55%,#4f4a3a 100%)}
.post .body{background:var(--white);box-shadow:var(--card-shadow);height:92px;padding:16px 18px 0}
.post h4{font-size:11px;font-weight:600;line-height:17px;color:#555}
.post .meta{margin-top:11px;display:flex;justify-content:space-between;font-size:9.5px;color:var(--muted)}
.post .meta .cat{color:var(--brand)}
.post .btn-cyan{height:34px}
</style>
</head>
<body>
<header class="abs hero" role="img" aria-label="Two children reading books in a sunlit green forest"></header>
<h1 class="abs hero-title">Teach english in South Korea</h1>
<nav class="abs crumbs">Home<span class="sep">•</span>Asia<span class="sep">•</span>Teach English online<span class="sep">•</span><span class="current">South Korea</span></nav>

<h2 class="abs intro-title">Do you need a VISA to teach English abroad ?</h2>
<p class="abs intro-sub">Lorem ipsum dolor sit amet consectetur. Mauris faucibus sed neque consequat.</p>
<div class="abs intro-body">
<p>Lorem ipsum dolor sit amet consectetur. A viverra in sagittis erat mus natoque luctus fermentum vel. Consectetur orci risus eget facilisis arcu.</p>
<p>Ac tristique sagittis augue porta luctus luctus lectus. Elementum et auctor nunc ultrices.</p>
<p>Enim ullamcorper aenean pulvinar cursus pellentesque sed interdum. Porta sit amet morbi aliquet felis vel turpis netus mattis. Libero nibh enim rhoncus quam morbi</p>
<p>sem diam urna senectus. Pulvinar dui neque eu amet sed aliquam. Sed lacus risus id volutpat mattis. Blandit consequat tortor etiam egestas eget. Cursus sagittis praesent est accumsan posuere nibh morbi morbi id. Pellentesque tellus rhoncus gravida elementum.</p>
<p>Posuere amet lorem. <a href="#">Aliquam nam dignissim sollicitudin et morbi orci</a>. Integer sed faucibus maecenas <a href="#">dolor placerat viverra</a> placerat. Sit congue enim venenatis id nullam ac donec commodo.</p>
<p>Consectetur tristique dolor cras porttitor vulputate nulla volutpat. Dictum vitae non odio sem odio ut bibendum. Sem in sed gravida phasellus eget libero at. Turpis sed condimentum integer lacus sed duis habitant faucibus aliquam. Diam tortor pellentesque nullam ac. Risus eu sit at aenean scelerisque vitae morbi. Sed fusce risus ut sit in tristique et ornare risus in urna in enim.</p>
</div>
<a class="abs btn-cyan intro-btn">How TEFL works›</a>

<section class="abs cta">
  <div class="cta-bg" role="img" aria-label="Hand writing in a spiral notebook beside a phone on a light speckled desk"></div>
  <h2 class="abs cta-title">Call to action</h2>
  <p class="abs cta-text">Loremed ut perspiciatis unde omnis iste natus error sit voluptatem accusantium doloremque laudantium, totam rem aperiam, eaque ipsa quae ab illo inventore veritatis et quasi architecto beata.</p>
  <a class="abs cta-btn">Click Here</a>
</section>

<h2 class="abs section-title" style="top:1170px">Teaching jobs in South Korea</h2>
<article class="abs job" style="left:83px;top:1260px"><h3>Lorem ipsum dolor sit amet consectetur. In scelerisque amet cum enim pretium faucibus</h3><div class="meta"><span class="loc">Japan</span><span>Posted 5 days ago</span><span>Internation TEFL Acedamy</span></div></article>
<article class="abs job" style="left:619px;top:1260px"><h3>Lorem ipsum dolor sit amet consectetur. In scelerisque amet cum enim pretium faucibus</h3><div class="meta"><span class="loc">Japan</span><span>Posted 5 days ago</span><span>Internation TEFL Acedamy</span></div></article>
<article class="abs job" style="left:83px;top:1420px"><h3>Lorem ipsum dolor sit amet consectetur. In scelerisque amet cum enim pretium faucibus</h3><div class="meta"><span class="loc">Japan</span><span>Posted 5 days ago</span><span>Internation TEFL Acedamy</span></div></article>
<article class="abs job" style="left:619px;top:1420px"><h3>Lorem ipsum dolor sit amet consectetur. In scelerisque amet cum enim pretium faucibus</h3><div class="meta"><span class="loc">Japan</span><span>Posted 5 days ago</span><span>Internation TEFL Acedamy</span></div></article>
<article class="abs job" style="left:83px;top:1580px"><h3>Lorem ipsum dolor sit amet consectetur. In scelerisque amet cum enim pretium faucibus</h3><div class="meta"><span class="loc">Japan</span><span>Posted 5 days ago</span><span>Internation TEFL Acedamy</span></div></article>
<article class="abs job" style="left:619px;top:1580px"><h3>Lorem ipsum dolor sit amet consectetur. In scelerisque amet cum enim pretium faucibus</h3><div class="meta"><span class="loc">Japan</span><span>Posted 5 days ago</span><span>Internation TEFL Acedamy</span></div></article>

<h2 class="abs section-title" style="top:1797px">Other popular &nbsp;places to teach in Asia</h2>
<a class="abs view-all">View all</a>
<a class="abs place" style="left:81px;top:1856px"><div class="ph" role="img" aria-label="Modern campus building among tall trees" style="background:linear-gradient(160deg,#4a5536,#2e3524 60%,#5a5648)"></div><span>Seoul</span></a>
<a class="abs place" style="left:344px;top:1856px"><div class="ph" role="img" aria-label="Campus building with autumn trees" style="background:linear-gradient(160deg,#c9a26a,#a7784a 50%,#8b8f7a)"></div><span>Seoul</span></a>
<a class="abs place" style="left:607px;top:1856px"><div class="ph" role="img" aria-label="Columned university hall behind green trees" style="background:linear-gradient(160deg,#7d8f4e,#8b7a5e 55%,#b9ad8c)"></div><span>Seoul</span></a>
<a class="abs place" style="left:870px;top:1856px"><div class="ph" role="img" aria-label="Red brick college building under blue sky" style="background:linear-gradient(160deg,#6f8fbf,#b0704e 55%,#6c5a48)"></div><span>Seoul</span></a>
<a class="abs place" style="left:81px;top:1990px"><div class="ph" role="img" aria-label="Brick school building with autumn foliage" style="background:linear-gradient(160deg,#9a6a48,#b5533e 55%,#6d5a46)"></div><span>Seoul</span></a>
<a class="abs place" style="left:344px;top:1990px"><div class="ph" role="img" aria-label="Pale campus buildings with blossoming trees" style="background:linear-gradient(180deg,#d7d6d4,#c9b7b0 55%,#8b8578)"></div><span>Seoul</span></a>
<a class="abs place" style="left:607px;top:1990px"><div class="ph" role="img" aria-label="Historic stone faculty building with bare trees" style="background:linear-gradient(160deg,#bdb8ae,#8d8579 55%,#4e4a40)"></div><span>Seoul</span></a>
<a class="abs place" style="left:870px;top:1990px"><div class="ph" role="img" aria-label="Campus building with autumn trees" style="background:linear-gradient(160deg,#c9a26a,#a7784a 50%,#8b8f7a)"></div><span>Seoul</span></a>

<h2 class="abs section-title" style="top:2176px">Related posts</h2>
<article class="abs post" style="left:81px;top:2242px"><div class="ph" role="img" aria-label="Modern campus building among tall trees"></div><div class="body"><h4>Lorem ipsum dolor sit amet consectetur.</h4><div class="meta"><span class="cat">Lorem imasets</span><span>Mar 28, 2023</span></div></div><a class="btn-cyan">Read more›</a></article>
<article class="abs post" style="left:345px;top:2242px"><div class="ph" role="img" aria-label="Modern campus building among tall trees"></div><div class="body"><h4>Lorem ipsum dolor sit amet consectetur.</h4><div class="meta"><span class="cat">Lorem imasets</span><span>Mar 28, 2023</span></div></div><a class="btn-cyan">Read more›</a></article>
<article class="abs post" style="left:607px;top:2242px"><div class="ph" role="img" aria-label="Modern campus building among tall trees"></div><div class="body"><h4>Lorem ipsum dolor sit amet consectetur.</h4><div class="meta"><span class="cat">Lorem imasets</span><span>Mar 28, 2023</span></div></div><a class="btn-cyan">Read more›</a></article>
<article class="abs post" style="left:870px;top:2242px"><div class="ph" role="img" aria-label="Modern campus building among tall trees"></div><div class="body"><h4>Lorem ipsum dolor sit amet consectetur.</h4><div class="meta"><span class="cat">Lorem imasets</span><span>Mar 28, 2023</span></div></div><a class="btn-cyan">Read more›</a></article>
</body>
</html>
```